small auto electrical company needs new logo and business cards !!!

we are a small auto electrical company (Velmor Autos Ltd) that has been running for 13 years the logo we have was put together by dinosaurs so we are looking at re branding the company starting with business cards and a new logo we fit GPS tracking devices for young drivers through there insurance company also we fit hands free systems and dash cameras also safety locks to fleet vehicles we would like bright eye catching colours day glow and neon and quirky designs for the logo our original logo was baby blue which i have added a picture enclosed we would like double sided but have a space to write notes and prices preferably not white on back same colour throughout many thanks
Reason: Just a chance to finalise any designs we want VA logos or V logos - No vlm's and no dinosaurs lol
Business
Installs@velmorautos.co.uk
07922483617
www.Velmorautos.co.uk
Velmor Autos Ltd - Fleets and Insurance Services
- new logo design !!
- Satellite in logo or something attaining to gps
- maybe a car in the logo
- shouldnt have velmor as vlm it is VeLMOR Autos

```html
<!DOCTYPE html>
<html lang="en">
<head>
<meta charset="utf-8">
<title>Velmor Autos Ltd – Business Cards</title>
<link rel="stylesheet" href="https://fonts.googleapis.com/css2?family=Orbitron:wght@700&family=Aldrich&display=swap">
<style>
  :root {
    --canvas-bg: #ecebee;
    --card-purple: #661f77;
    --card-purple-deep: #561866;
    --swoosh-light: #e6e6e8;
    --swoosh-mid: #a9a9ad;
    --swoosh-dark: #3a3a3d;
    --brand-blue: #62d3f0;
    --offer-orange: #ff4a1c;
    --service-green: #62d64a;
    --badge-blue: #1c86e6;
    --badge-yellow: #f4f21c;
  }
  * { box-sizing: border-box; margin: 0; padding: 0; }
  html, body { width: 1200px; height: 676px; overflow: hidden; }
  body {
    background: var(--canvas-bg);
    position: relative;
    font-family: "Aldrich", "Arial", sans-serif;
  }
  .card {
    position: absolute;
    top: 163px;
    width: 540px;
    height: 350px;
    background: linear-gradient(160deg, var(--card-purple) 0%, var(--card-purple-deep) 100%);
    overflow: hidden;
    box-shadow: 0 6px 18px rgba(0,0,0,0.18);
  }
  .card--front { left: 40px; }
  .card--back { left: 620px; }
  .card__swoosh { position: absolute; inset: 0; width: 100%; height: 100%; }

  /* Front */
  .brand-mark {
    position: absolute;
    left: 226px;
    top: 34px;
    width: 88px;
    height: 88px;
    border-radius: 50%;
    background: var(--brand-blue);
  }
  .brand-name {
    position: absolute;
    left: 20px;
    top: 138px;
    width: 500px;
    font-family: "Orbitron", "Arial", sans-serif;
    font-weight: 700;
    color: var(--brand-blue);
    text-align: center;
    line-height: 1;
    white-space: nowrap;
  }
  .brand-name__title { font-size: 31px; letter-spacing: 1.5px; display: block; }
  .brand-name__tagline { font-size: 15px; letter-spacing: 1.5px; display: block; margin-top: 12px; }

  /* Back */
  .offer-heading {
    position: absolute;
    left: 48px;
    top: 36px;
    font-size: 28px;
    color: var(--offer-orange);
    font-style: italic;
    white-space: nowrap;
  }
  .service-list {
    position: absolute;
    left: 48px;
    top: 90px;
    list-style: none;
    color: var(--service-green);
    font-size: 23px;
    line-height: 1.25;
    white-space: nowrap;
  }
  .service-list li { position: relative; padding-left: 22px; }
  .service-list li::before {
    content: "";
    position: absolute;
    left: 0;
    top: 9px;
    width: 12px;
    height: 12px;
    border-radius: 50%;
    background: var(--offer-orange);
  }
  .experience-badge {
    position: absolute;
    right: 36px;
    top: 205px;
    width: 176px;
    padding: 8px 0 10px;
    background: var(--badge-blue);
    border-radius: 8px;
    color: var(--badge-yellow);
    text-align: center;
    line-height: 1.05;
  }
  .experience-badge__years { display: block; font-size: 28px; letter-spacing: 1px; }
  .experience-badge__label { display: block; font-size: 19px; letter-spacing: 1px; }
  .brand-small {
    position: absolute;
    right: 36px;
    top: 124px;
    display: flex;
    align-items: center;
    gap: 6px;
    font-family: "Orbitron", "Arial", sans-serif;
    font-weight: 700;
    color: var(--brand-blue);
    line-height: 1;
    white-space: nowrap;
  }
  .brand-small__mark { width: 24px; height: 24px; border-radius: 50%; background: var(--brand-blue); }
  .brand-small__text { font-size: 12px; }
  .brand-small__text small { display: block; font-size: 7px; margin-top: 3px; }
</style>
</head>
<body>
  <section class="card card--front" aria-label="Business card front">
    <svg class="card__swoosh" viewBox="0 0 540 350" preserveAspectRatio="none" aria-hidden="true">
      <path d="M0 250 C160 258 300 300 540 220 L540 350 L0 350 Z" fill="var(--swoosh-light)"/>
      <path d="M0 270 C170 276 320 318 540 244 L540 350 L0 350 Z" fill="var(--swoosh-mid)"/>
      <path d="M230 350 C360 340 460 305 540 268 L540 350 Z" fill="var(--swoosh-dark)"/>
    </svg>
    <div class="brand-mark"></div>
    <h1 class="brand-name">
      <span class="brand-name__title">VELMOR AUTOS LTD</span>
      <span class="brand-name__tagline">FLEET &amp; INSURANCE SERVICE</span>
    </h1>
  </section>

  <section class="card card--back" aria-label="Business card back">
    <svg class="card__swoosh" viewBox="0 0 540 350" preserveAspectRatio="none" aria-hidden="true">
      <path d="M120 0 C260 40 380 120 540 110 L540 0 Z" fill="var(--swoosh-light)"/>
      <path d="M220 0 C320 30 420 95 540 88 L540 0 Z" fill="var(--swoosh-mid)"/>
      <path d="M360 0 C420 25 480 55 540 60 L540 0 Z" fill="var(--swoosh-dark)"/>
    </svg>
    <div class="brand-small">
      <span class="brand-small__mark"></span>
      <span class="brand-small__text">VELMOR AUTOS LTD<small>FLEET &amp; INSURANCE SERVICE</small></span>
    </div>
    <h2 class="offer-heading">We offer to fit</h2>
    <ul class="service-list">
      <li>GPS tracking devices</li>
      <li>Hands free systems</li>
      <li>Dash cameras</li>
      <li>Safety locks</li>
    </ul>
    <div class="experience-badge">
      <span class="experience-badge__years">13 YEARS</span>
      <span class="experience-badge__label">EXPERIENCE</span>
    </div>
  </section>
</body>
</html>
```